Modern, eye catching eliquid bottle label. 1.5 x 2.75

We need a label design for our e-juice bottles. The labels to be printed are 1.5 inches in height and 2.75 inches in width. We are looking to include our website (www.quillbrookmistparlor.com) and our phone number of 2 different shops. The most prominent thing needs to be our logo(attached .pdf and jpeg). We will need 2 spots that we can edit on an ongoing basis for nicotine strength and the flavor. We want something simplistic but eye-catching. Our colors are Purple, Red, and Orange. We would also like our website fairly prominent as well.

Target Market(s)

18-45 vapers and e-cigarette users

Font styles to use
Serif

Colors
6b449b
f78e1f
ec1f27
ffffff
000000

Requirements
Must have
• eye catching
• "Quillbrook Mist" must be LARGE
• phone number
• website
• areas for flavor name and nicotine strength
• orange, purple, black and red
Nice to have
• clean, abstract vectors
• "corporate look"
• think of a DUNTRA FIZZ can, you immediately know what your'e looking at.
• Our V in vapor is our go to logo
Should not have
• no grunge effects
• no round shapes

```html
<!DOCTYPE html>
<html lang="en">
<head>
<meta charset="utf-8">
<title>Quillbrook Mist – E-liquid Bottle Label</title>
<link rel="stylesheet" href="https://fonts.googleapis.com/css2?family=Yellowtail&family=Lobster+Two:ital,wght@0,400;1,700&family=Nunito:ital,wght@1,900&family=Kaushan+Script&display=block">
<style>
  :root {
    --brand-purple: #8e4fb3;
    --brand-orange: #f4a020;
    --brand-red: #ec1f27;
    --label-white: #ffffff;
  }
  html, body {
    margin: 0;
    padding: 0;
    overflow: hidden;
    background: var(--label-white);
  }
  .label {
    position: relative;
    width: 1200px;
    height: 670px;
    background: var(--label-white);
    overflow: hidden;
  }
  .phone {
    position: absolute;
    margin: 0;
    font-family: "Nunito", Arial, sans-serif;
    font-style: italic;
    font-weight: 900;
    font-size: 50px;
    letter-spacing: 8px;
    line-height: 1;
    white-space: nowrap;
    color: var(--brand-purple);
  }
  .phone--shop-one { left: 232px; top: 118px; }
  .phone--shop-two { left: 220px; top: 190px; }
  .brand {
    position: absolute;
    left: 95px;
    top: 270px;
    display: flex;
    align-items: center;
    gap: 34px;
  }
  .brand-name {
    margin: 0;
    font-family: "Yellowtail", "Lobster Two", cursive;
    font-weight: 400;
    font-size: 150px;
    line-height: 1.2;
    white-space: nowrap;
    color: var(--brand-purple);
  }
  .brand-mark {
    flex: none;
    width: 96px;
    height: 96px;
    background: var(--brand-red);
  }
  .website {
    position: absolute;
    left: 0;
    width: 1170px;
    top: 488px;
    margin: 0;
    text-align: center;
    font-family: "Lobster Two", cursive;
    font-style: italic;
    font-weight: 700;
    font-size: 80px;
    letter-spacing: 2px;
    line-height: 1;
    white-space: nowrap;
    color: var(--brand-orange);
    text-shadow: -2px 2px 0 var(--brand-purple);
  }
  .product-detail {
    position: absolute;
    top: 578px;
    margin: 0;
    font-family: "Kaushan Script", cursive;
    font-size: 45px;
    line-height: 1;
    white-space: nowrap;
    color: var(--brand-purple);
  }
  .product-detail--flavor { left: 55px; }
  .product-detail--strength { left: 812px; }
</style>
</head>
<body>
  <main class="label">
    <p class="phone phone--shop-one">(555) 555-5555</p>
    <p class="phone phone--shop-two">(555) 555-5555</p>
    <div class="brand">
      <h1 class="brand-name">Quillbrook Mist</h1>
      <span class="brand-mark" aria-hidden="true"></span>
    </div>
    <p class="website">www.quillbrookmistparlor.com</p>
    <p class="product-detail product-detail--flavor">Chocolate Hazelberry</p>
    <p class="product-detail product-detail--strength">140mg Nicotine</p>
  </main>
</body>
</html>
```